BRISKLE sparkling water needs new artwork! Based in Southern California

"Briskle" is a new sparkling water company based in Southern California that offers refreshing flavors (lime, cherry, & mango) with B vitamins and antioxidants.

We would like to see packaging designs for standard 12oz cans for each of the three flavors.
Our initial preference is to have individual artwork for each flavor.

Attached are examples of competitors' designs.
Updates

We are extending the deadline for the Thanksgiving Holiday. Thank you all for your contributions.

```html
<!DOCTYPE html>
<html lang="en">
<head>
<meta charset="utf-8">
<title>Briskle Sparkling Water – Can Labels</title>
<link rel="stylesheet" href="https://fonts.googleapis.com/css2?family=Montserrat:wght@900&family=Kaushan+Script&family=Anton&family=Barlow+Semi+Condensed:wght@600&family=Arimo:wght@700&display=swap">
<style>
  :root {
    --backdrop: #e0ded8;
    --navy: #3b5378;
    --ink: #1e1e1e;
    --text-dark: #2a2a2a;
    --mango-top: #dcdcd2;
    --mango-bottom: #e2a443;
    --lime-top: #e2ecd4;
    --lime-bottom: #7fae45;
    --cherry-top: #d9dcd8;
    --cherry-bottom: #8e3f50;
    --sun-yellow: #f2c418;
    --sun-orange: #e6892c;
    --sun-red: #c62a12;
  }
  * { margin: 0; padding: 0; box-sizing: border-box; }
  html, body {
    width: 1200px; height: 1200px; overflow: hidden;
    background: var(--backdrop);
  }
  .label-lineup {
    position: relative; width: 1200px; height: 1200px;
  }
  .can-label {
    position: absolute; top: 330px;
    width: 350px; height: 560px;
    border-radius: 18px;
    overflow: hidden;
  }
  .can-label--mango  { left: 50px;  background: linear-gradient(180deg, var(--mango-top) 0%, #ecd4a8 45%, var(--mango-bottom) 100%); }
  .can-label--lime   { left: 425px; background: linear-gradient(180deg, var(--lime-top) 0%, #c9dfa8 50%, var(--lime-bottom) 100%); }
  .can-label--cherry { left: 800px; background: linear-gradient(180deg, var(--cherry-top) 0%, #cda9b0 55%, var(--cherry-bottom) 100%); }

  .brand-name {
    position: absolute; left: 14px; top: 70px;
    writing-mode: vertical-rl; transform: rotate(180deg);
    font-family: "Montserrat", sans-serif; font-weight: 900;
    font-size: 62px; line-height: 1; letter-spacing: 2px;
    color: var(--navy);
  }
  .sunset-emblem {
    position: absolute; left: 100px; top: 70px;
    width: 225px; height: 225px;
  }
  .product-type {
    position: absolute; left: 62px; right: 6px; top: 318px;
    text-align: center;
    font-family: "Kaushan Script", cursive; font-size: 34px;
    color: var(--ink);
    text-shadow: 2px 0 #fff, -2px 0 #fff, 0 2px #fff, 0 -2px #fff;
  }
  .flavor-name {
    position: absolute; left: 80px; right: 0; top: 380px;
    text-align: center;
    font-family: "Anton", sans-serif; font-size: 46px; letter-spacing: 2px;
    color: var(--ink);
  }
  .benefits {
    position: absolute; left: 80px; right: 0; top: 446px;
    text-align: center;
    font-family: "Barlow Semi Condensed", sans-serif; font-weight: 600;
    font-size: 15px; letter-spacing: 0.3px;
    color: var(--text-dark);
  }
  .dotted-rule {
    position: absolute; left: 0; right: 0; top: 482px;
    border-top: 4px dotted var(--text-dark);
  }
  .volume {
    position: absolute; left: 80px; right: 0; top: 500px;
    text-align: center;
    font-family: "Arimo", sans-serif; font-weight: 700; font-size: 18px;
    color: var(--text-dark);
  }
</style>
</head>
<body>
<main class="label-lineup">

  <section class="can-label can-label--mango">
    <div class="brand-name">BRISKLE</div>
    <svg class="sunset-emblem" viewBox="0 0 100 100" role="img" aria-label="Striped sunset emblem with palm tree silhouettes">
      <defs>
        <linearGradient id="sunset-mango" x1="0" y1="0" x2="0" y2="1">
          <stop offset="0" stop-color="#3b5378"/>
          <stop offset="0.3" stop-color="#f2c418"/>
          <stop offset="0.7" stop-color="#e6892c"/>
          <stop offset="1" stop-color="#c62a12"/>
        </linearGradient>
      </defs>
      <circle cx="50" cy="50" r="50" fill="url(#sunset-mango)"/>
    </svg>
    <div class="product-type">Sparkling Water</div>
    <div class="flavor-name">MANGO</div>
    <div class="benefits">B VITAMINS &amp; ANTIOXIDANTS</div>
    <div class="dotted-rule"></div>
    <div class="volume">12 fl oz ( 355ml)</div>
  </section>

  <section class="can-label can-label--lime">
    <div class="brand-name">BRISKLE</div>
    <svg class="sunset-emblem" viewBox="0 0 100 100" role="img" aria-label="Striped sunset emblem with palm tree silhouettes">
      <defs>
        <linearGradient id="sunset-lime" x1="0" y1="0" x2="0" y2="1">
          <stop offset="0" stop-color="#3b5378"/>
          <stop offset="0.3" stop-color="#f2c418"/>
          <stop offset="0.7" stop-color="#e6892c"/>
          <stop offset="1" stop-color="#c62a12"/>
        </linearGradient>
      </defs>
      <circle cx="50" cy="50" r="50" fill="url(#sunset-lime)"/>
    </svg>
    <div class="product-type">Sparkling Water</div>
    <div class="flavor-name">LIME</div>
    <div class="benefits">B VITAMINS &amp; ANTIOXIDANTS</div>
    <div class="dotted-rule"></div>
    <div class="volume">12 fl oz ( 355ml)</div>
  </section>

  <section class="can-label can-label--cherry">
    <div class="brand-name">BRISKLE</div>
    <svg class="sunset-emblem" viewBox="0 0 100 100" role="img" aria-label="Striped sunset emblem with palm tree silhouettes">
      <defs>
        <linearGradient id="sunset-cherry" x1="0" y1="0" x2="0" y2="1">
          <stop offset="0" stop-color="#3b5378"/>
          <stop offset="0.3" stop-color="#f2c418"/>
          <stop offset="0.7" stop-color="#e6892c"/>
          <stop offset="1" stop-color="#c62a12"/>
        </linearGradient>
      </defs>
      <circle cx="50" cy="50" r="50" fill="url(#sunset-cherry)"/>
    </svg>
    <div class="product-type">Sparkling Water</div>
    <div class="flavor-name">CHERRY</div>
    <div class="benefits">B VITAMINS &amp; ANTIOXIDANTS</div>
    <div class="dotted-rule"></div>
    <div class="volume">12 fl oz ( 355ml)</div>
  </section>

</main>
</body>
</html>
```